FCA Sign 24”x60”

We need a design for our FCA sign (24”x60”) that is going next to a table (attached is an image of the sign)

I'd like the color scheme to royal blue in the website below and I've attached a few of our school logos.

It should have the colors and simple FCA logo of this tablecloth https://shop.vendlora.com/items.lasso?c_id=Tablecloths&-session=QR_Buyers:4FD2837A248ac9E51WpYNJ7B049C

The most important thing is the words pop and is easy to read from far away.

Wexbrook FCA

What do we do?
Help at school events
Support our school and students
Organize fundraising events
Have fun together!

Questions? Email FCAWexbrook@mailvera.com

Get text updates - Text @wexbrookfca to the number 47392

Target Market(s)

Parents of Elementary School Students

Industry/Entity Type

Education

Font styles to use
Sans Serif

Colors

Designer to choose colors to be used in the design.

Requirements
Must have
• Clear words that pop- easy to read

```html
<!DOCTYPE html>
<html lang="en">
<head>
<meta charset="utf-8">
<title>Wexbrook FCA – Table Sign</title>
<link href="https://fonts.googleapis.com/css2?family=Inter:wght@300;400;700;800;900&display=swap" rel="stylesheet">
<style>
  :root {
    --navy: #262a68;
    --red: #ed1c24;
    --white: #ffffff;
    --ring: #c9c9cf;
    --stage: #ececec;
  }
  * { margin: 0; padding: 0; box-sizing: border-box; }
  html, body { width: 1200px; height: 1200px; overflow: hidden; background: var(--stage); }
  body { font-family: "Inter", Arial, sans-serif; color: var(--white); }

  .sign {
    position: absolute; left: 378px; top: 40px;
    width: 444px; height: 1120px;
    background: var(--navy); overflow: hidden;
  }
  .sign > * { position: absolute; }

  .title { right: 38px; text-align: right; line-height: 1; }
  .title-name { top: 38px; font-weight: 800; font-size: 60px; letter-spacing: -1px; }
  .title-org { top: 112px; font-weight: 900; font-style: italic; font-size: 94px; letter-spacing: -2px; }

  .question-band { left: 0; top: 230px; width: 444px; height: 161px; background: var(--red); }
  .question-band .stripe { position: absolute; top: 0; bottom: 0; width: 6px; background: var(--navy); }
  .question {
    left: 38px; top: 250px; font-weight: 300; font-size: 64px; line-height: 60px; letter-spacing: -1px;
  }
  .question strong { font-weight: 800; }

  .duties { left: 40px; top: 432px; width: 380px; list-style: none; }
  .duties li {
    position: relative; padding-left: 24px; font-weight: 700; font-size: 26px; line-height: 29px;
    margin-bottom: 28px;
  }
  .duties li::before {
    content: ""; position: absolute; left: 0; top: 10px; width: 11px; height: 11px;
    border-radius: 50%; background: var(--red);
  }

  .badge {
    top: 733px; width: 150px; height: 150px; border-radius: 50%;
    background: var(--white); border: 6px solid var(--ring);
    display: flex; align-items: center; justify-content: center;
  }
  .badge-mascot { left: 48px; }
  .badge-mascot .mascot-fill {
    width: 100px; height: 110px; border-radius: 40%;
    background: linear-gradient(160deg, #3a3f8f, #262a68 60%, #c8a03a);
  }
  .badge-school { left: 243px; }
  .badge-school span { color: var(--navy); font-weight: 800; font-size: 24px; line-height: 1.05; text-align: center; }

  .divider { left: 38px; top: 918px; width: 371px; height: 3px; background: var(--red); }

  .contact-icon { left: 38px; width: 44px; height: 44px; }
  .contact-text { left: 118px; }
  .contact-text h3 { font-weight: 700; font-size: 22px; line-height: 1.2; }
  .contact-text p { font-weight: 700; font-size: 16px; line-height: 1.3; }
  .contact-text .number { font-size: 22px; line-height: 1.1; }
</style>
</head>
<body>
  <main class="sign">
    <div class="title title-name">WEXBROOK</div>
    <div class="title title-org">FCA</div>

    <div class="question-band">
      <span class="stripe" style="left:378px"></span>
      <span class="stripe" style="left:396px"></span>
      <span class="stripe" style="left:414px"></span>
      <span class="stripe" style="left:432px"></span>
    </div>
    <h2 class="question">What do<br>we <strong>do</strong>?</h2>

    <ul class="duties">
      <li>Help at school events</li>
      <li>Support our school and students</li>
      <li>Organize fundraising events</li>
      <li>Have fun together!</li>
    </ul>

    <div class="badge badge-mascot">
      <div class="mascot-fill" role="img" aria-label="School mascot illustration in graduation cap"></div>
    </div>
    <div class="badge badge-school"><span>Bright<br>Path</span></div>

    <div class="divider"></div>

    <svg class="contact-icon" style="top:941px" viewBox="0 0 44 44" aria-hidden="true">
      <circle cx="22" cy="22" r="21" fill="#fff"/>
      <text x="22" y="31" text-anchor="middle" font-family="Inter, Arial, sans-serif" font-weight="800" font-size="26" fill="#262a68">?</text>
    </svg>
    <div class="contact-text" style="top:934px">
      <h3>Questions?</h3>
      <p>Email FCAWexbrook@mailvera.com</p>
    </div>

    <svg class="contact-icon" style="top:1022px" viewBox="0 0 44 44" aria-hidden="true">
      <circle cx="22" cy="22" r="21" fill="#fff"/>
      <rect x="14" y="10" width="16" height="24" rx="3" fill="none" stroke="#262a68" stroke-width="2.5"/>
      <line x1="18" y1="17" x2="26" y2="17" stroke="#262a68" stroke-width="2"/>
      <line x1="18" y1="21" x2="26" y2="21" stroke="#262a68" stroke-width="2"/>
      <line x1="18" y1="25" x2="24" y2="25" stroke="#262a68" stroke-width="2"/>
    </svg>
    <div class="contact-text" style="top:1015px">
      <h3>Get Text Updates</h3>
      <p>Text @wexbrookfca to the number</p>
      <p class="number">47392</p>
    </div>
  </main>
</body>
</html>
```